One Page flat design for Car Classified Site

I'm looking for a flat design that that is very simple on the eye but with style. I need it to have a footer for some links etc, and the header needs a new feel but nothing to major.
This one page design is needed for the main page of the classified site...after this page is correct then all the other pages need to be designed to follow a similar style (new work).
I want more emphasis on the text rather than the images as a lot of users don't add images of the vehicles.
Attached is a mock up of the information and rough layout.
Wheelmarketlane.com is a classified site for car dealers only, I've also attached how the main competitions site looks.
Target Market(s)
Middle aged men, these guys are car dealers so it needs to be basic and easy for them as they aren't techie types.
Industry/Entity Type
Work
Number of Pages Required
1 page
Font styles to use
Look and feel

```html
<!DOCTYPE html>
<html lang="en">
<head>
<meta charset="utf-8">
<title>Wheel Market Lane – Search Results</title>
<link href="https://fonts.googleapis.com/css2?family=Source+Sans+3:wght@400;600;700&display=swap" rel="stylesheet">
<style>
:root{
  --blue:#1a8ad4;
  --blue-dark:#1479bd;
  --teal:#22a3c9;
  --red:#ee3a36;
  --red-soft:#f6625d;
  --ink:#2b2b2b;
  --text:#444;
  --muted:#777;
  --line:#cfcfcf;
  --bar:#d6d6d6;
  --page:#f3f3f3;
  --white:#fff;
}
*{box-sizing:border-box;margin:0;padding:0}
html,body{width:877px;height:1200px;overflow:hidden}
body{position:relative;background:var(--page);font-family:"Source Sans 3",Arial,sans-serif;color:var(--text);font-size:9px}
.abs{position:absolute}
/* header */
.site-header{left:0;top:0;width:877px;height:61px;background:var(--white)}
.brand{left:129px;top:14px;font-size:28px;font-weight:700;color:var(--ink);letter-spacing:-.5px}
.utility{right:131px;top:8px;font-size:7px;color:var(--muted)}
.utility span{margin:0 5px}
.welcome{right:131px;top:27px;font-size:8px;color:var(--text);display:flex;align-items:center;gap:4px}
.welcome b{color:var(--ink)}
.welcome i{display:inline-block;width:11px;height:11px;border:1px solid #aaa;border-radius:50%}
.main-nav{left:0;top:61px;width:877px;height:28px;background:var(--blue);display:flex;padding-left:129px}
.main-nav a{color:var(--white);font-size:9.5px;font-weight:700;text-decoration:none;line-height:28px;padding:0 15px;border-right:1px solid var(--blue-dark)}
.main-nav a:first-child{padding-left:0}
.main-nav a:last-child{border:none}
/* hero */
.hero{left:0;top:89px;width:877px;height:163px;background:linear-gradient(90deg,#9ea4a8 0%,#c9cfd2 30%,#e8eaeb 55%,#dfe3e4 70%,#b9bda6 100%)}
.search-panel{left:130px;top:89px;width:331px;height:163px;background:rgba(40,40,40,.85);padding:12px 13px}
.search-panel h2{color:var(--white);font-size:12.5px;font-weight:700;margin-bottom:9px}
.fields{display:grid;grid-template-columns:148px 148px;gap:8px 8px}
.field{height:23px;background:var(--white);border-radius:2px;font-size:8.5px;color:var(--text);padding:0 8px;display:flex;align-items:center;justify-content:space-between}
.field svg{width:7px;height:5px}
.search-btn{margin-top:9px;width:82px;height:23px;background:var(--teal);color:var(--white);font-size:11px;font-weight:700;border-radius:2px;display:flex;align-items:center;justify-content:center}
.hero-photo{left:461px;top:89px;width:416px;height:163px;background:linear-gradient(100deg,#c7ccd0 0%,#e6e8e9 40%,#d4553f 60%,#2a2a2a 80%,#cfd3c4 100%);opacity:.9}
/* pagination */
.pager{left:130px;display:flex;gap:6px;align-items:center}
.pager span{height:18px;min-width:22px;border:1px solid var(--line);background:var(--white);font-size:8px;color:var(--blue);display:flex;align-items:center;justify-content:center;font-weight:600}
.pager .wide{width:39px}
.pager .current{background:var(--teal);color:var(--white);border-color:var(--teal)}
.pager .dots{border:none;background:none;min-width:8px;color:#888}
.result-count{right:130px;top:268px;font-size:8px;color:var(--ink)}
.result-count em{font-style:normal;color:var(--blue);font-weight:600}
/* listing */
.listing{left:130px;width:616px;height:221px;background:var(--white);border:1px solid var(--line)}
.badge-new{position:absolute;right:12px;top:-23px;width:44px;height:24px}
.listing-head{height:26px;background:var(--bar);display:flex;justify-content:space-between;align-items:center;padding:0 15px 0 11px}
.listing-head h3{font-size:11px;font-weight:700;color:var(--ink)}
.listing-head p{font-size:11px;color:var(--ink)}
.thumb{position:absolute;left:11px;top:40px;width:114px;height:114px;border:1px solid var(--line);display:flex;align-items:center;justify-content:center}
.spec-row{position:absolute;left:139px;top:43px;display:flex;font-size:8.5px;white-space:nowrap}
.spec-row span{padding:0 15px;border-left:1px solid var(--line)}
.spec-row span:first-child{padding-left:0;border:none}
.col{position:absolute;top:64px;width:115px;font-size:8.5px}
.col h4{font-size:8.5px;font-weight:700;color:var(--ink);display:flex;align-items:center;gap:4px;padding-bottom:3px;border-bottom:1px solid var(--line);margin-bottom:5px}
.col h4 svg{width:9px;height:9px}
.col li{list-style:none;line-height:18px}
.col li.strong{font-weight:700;line-height:12px;padding-top:3px;color:var(--ink)}
.col-history{left:139px}
.col-seller{left:276px;width:132px}
.comments{position:absolute;left:11px;top:178px;width:398px;border-top:1px solid var(--line);padding-top:7px;padding-right:8px;font-size:8.5px;line-height:18px;color:var(--ink)}
.comments b{font-weight:700}
.deal-box{position:absolute;left:418px;top:42px;width:189px;height:163px;background:var(--red);text-align:center;color:var(--white);padding-top:13px}
.deal-box h5{font-size:12.5px;font-weight:700;line-height:15px}
.deal-box h6{font-size:12.5px;font-weight:400;line-height:17px}
.prices{display:flex;justify-content:center;gap:9px;margin-top:7px}
.price{width:74px;height:33px;background:var(--red-soft);font-size:9.5px;line-height:12px;padding-top:4px}
.price b{display:block;font-weight:700}
.guide{font-size:7px;margin-top:6px}
.details-btn{margin:9px auto 0;width:156px;height:25px;background:#111;color:var(--white);font-size:11px;font-weight:700;line-height:25px;border-radius:2px}
/* footer */
.site-footer{left:0;top:1079px;width:877px;height:91px;background:var(--white);border-top:1px solid #e2e2e2}
.foot-col{position:absolute;top:13px;font-size:7px;color:var(--text);line-height:12.5px}
.foot-col h4{font-size:8.5px;font-weight:700;color:var(--ink);margin-bottom:3px}
.foot-col b{color:var(--ink)}
.socials{display:flex;gap:5px;margin-top:2px}
.socials i{width:15px;height:15px;border-radius:50%;display:block}
.copyright{left:0;top:1170px;width:877px;height:30px;background:#e8e8e8;text-align:center;line-height:30px;font-size:7px;color:var(--text)}
</style>
</head>
<body>

<header class="abs site-header">
  <div class="abs brand">Wheel Market Lane</div>
  <div class="abs utility">Messages<span>|</span>Inbox<span>|</span>Contact Us</div>
  <div class="abs welcome">Welcome <b>User</b> <i></i></div>
</header>
<nav class="abs main-nav">
  <a>Home</a><a>About Us</a><a>Our Services</a><a>Dealers</a><a>Deals</a><a>MyAds</a><a>Account</a><a>Contact Us</a>
</nav>

<div class="abs hero" role="img" aria-label="Open road stretching to the horizon under a pale sky"></div>
<div class="abs hero-photo" role="img" aria-label="Red sports coupe presented by a sales consultant"></div>
<form class="abs search-panel">
  <h2>Search Cars</h2>
  <div class="fields">
    <div class="field">Make: Any <svg viewBox="0 0 7 5"><path d="M0 0h7L3.5 5z" fill="#999"/></svg></div>
    <div class="field">Price: Any <svg viewBox="0 0 7 5"><path d="M0 0h7L3.5 5z" fill="#999"/></svg></div>
    <div class="field">Body Type: Any <svg viewBox="0 0 7 5"><path d="M0 0h7L3.5 5z" fill="#999"/></svg></div>
    <div class="field">Model: Any <svg viewBox="0 0 7 5"><path d="M0 0h7L3.5 5z" fill="#999"/></svg></div>
    <div class="field">Age: Any <svg viewBox="0 0 7 5"><path d="M0 0h7L3.5 5z" fill="#999"/></svg></div>
    <div class="field">Keyword</div>
  </div>
  <div class="search-btn">Search</div>
</form>

<div class="abs pager" style="top:264px">
  <span class="wide">Prev</span><span class="current">1</span><span>2</span><span>3</span><span>4</span><span>5</span><span>6</span><span>7</span><span>8</span><span class="dots">...</span><span>25</span><span class="wide">Next</span>
</div>
<div class="abs result-count">Search Result Showing <em>1-25</em> og <em>2,000</em></div>

<article class="abs listing" style="top:313px">
  <svg class="badge-new" viewBox="0 0 44 24"><path d="M2 24A20 20 0 0 1 42 24z" fill="#22a3c9" stroke="#22a3c9" stroke-width="3" stroke-dasharray="2 2"/><text x="22" y="20" text-anchor="middle" font-size="8" font-weight="700" fill="#fff" font-family="Source Sans 3,Arial,sans-serif">NEW</text></svg>
  <div class="listing-head"><h3>2014 NORVAN KESTREL VERSA TDX</h3><p>Buy it now for € 13750 or please bid</p></div>
  <div class="thumb"><svg width="86" height="34" viewBox="0 0 86 34"><path d="M4 22l3-10 12-2 10-8h28l12 9 12 3 1 8H4z" fill="#a9a9a9"/><path d="M32 4h10v8H27zM45 4h10l8 8H45z" fill="#fff"/><circle cx="20" cy="26" r="7" fill="#a9a9a9" stroke="#fff" stroke-width="2"/><circle cx="66" cy="26" r="7" fill="#a9a9a9" stroke="#fff" stroke-width="2"/></svg></div>
  <div class="spec-row"><span>2007 (56)</span><span>58,000 Miles</span><span>Automatic</span><span>Grey</span></div>
  <ul class="col col-history"><h4><svg viewBox="0 0 10 10"><circle cx="5" cy="5" r="4" fill="none" stroke="#555" stroke-width="1.2"/><path d="M5 2.5V5h2" stroke="#555" fill="none"/></svg>HISTORY</h4><li>6 owners</li><li>NO SERVICE HISTORY</li><li>UK Vehicle</li><li class="strong">V5 NOT available due to cherished transfer</li></ul>
  <ul class="col col-seller"><h4><svg viewBox="0 0 10 10"><circle cx="5" cy="3" r="2.5" fill="#555"/><path d="M0 10a5 4 0 0 1 10 0z" fill="#555"/></svg>SELLER</h4><li>Specialist Dealer</li><li>East Yorkshire</li><li>214 Miles away</li><li>Joined 10 years ago</li><li>Holloway Vehicle Solutions Limited</li></ul>
  <p class="comments"><b>Comments:</b> Lorem Ipsum is simply dummy text of the printing and typesetting industry. Lorem Ipsum has been the industry's standard dummy text.</p>
  <div class="deal-box"><h5>Trying to Deal</h5><h6>My Customer</h6><div class="prices"><div class="price"><b>Trade Price</b>€ 15,750</div><div class="price"><b>Retail Price</b>€ 17,750</div></div><p class="guide">Guide Prices correct as of 02 Feb 2015</p><div class="details-btn">Full Details</div></div>
</article>

<article class="abs listing" style="top:566px">
  <svg class="badge-new" viewBox="0 0 44 24"><path d="M2 24A20 20 0 0 1 42 24z" fill="#22a3c9" stroke="#22a3c9" stroke-width="3" stroke-dasharray="2 2"/><text x="22" y="20" text-anchor="middle" font-size="8" font-weight="700" fill="#fff" font-family="Source Sans 3,Arial,sans-serif">NEW</text></svg>
  <div class="listing-head"><h3>2014 NORVAN KESTREL VERSA TDX</h3><p>Buy it now for € 13750 or please bid</p></div>
  <div class="thumb"><svg width="86" height="34" viewBox="0 0 86 34"><path d="M4 22l3-10 12-2 10-8h28l12 9 12 3 1 8H4z" fill="#a9a9a9"/><path d="M32 4h10v8H27zM45 4h10l8 8H45z" fill="#fff"/><circle cx="20" cy="26" r="7" fill="#a9a9a9" stroke="#fff" stroke-width="2"/><circle cx="66" cy="26" r="7" fill="#a9a9a9" stroke="#fff" stroke-width="2"/></svg></div>
  <div class="spec-row"><span>2007 (56)</span><span>58,000 Miles</span><span>Automatic</span><span>Grey</span></div>
  <ul class="col col-history"><h4><svg viewBox="0 0 10 10"><circle cx="5" cy="5" r="4" fill="none" stroke="#555" stroke-width="1.2"/><path d="M5 2.5V5h2" stroke="#555" fill="none"/></svg>HISTORY</h4><li>6 owners</li><li>NO SERVICE HISTORY</li><li>UK Vehicle</li><li class="strong">V5 NOT available due to cherished transfer</li></ul>
  <ul class="col col-seller"><h4><svg viewBox="0 0 10 10"><circle cx="5" cy="3" r="2.5" fill="#555"/><path d="M0 10a5 4 0 0 1 10 0z" fill="#555"/></svg>SELLER</h4><li>Specialist Dealer</li><li>East Yorkshire</li><li>214 Miles away</li><li>Joined 10 years ago</li><li>Holloway Vehicle Solutions Limited</li></ul>
  <p class="comments"><b>Comments:</b> Lorem Ipsum is simply dummy text of the printing and typesetting industry. Lorem Ipsum has been the industry's standard dummy text.</p>
  <div class="deal-box"><h5>Trying to Deal</h5><h6>My Customer</h6><div class="prices"><div class="price"><b>Trade Price</b>€ 15,750</div><div class="price"><b>Retail Price</b>€ 17,750</div></div><p class="guide">Guide Prices correct as of 02 Feb 2015</p><div class="details-btn">Full Details</div></div>
</article>

<article class="abs listing" style="top:820px">
  <svg class="badge-new" viewBox="0 0 44 24"><path d="M2 24A20 20 0 0 1 42 24z" fill="#22a3c9" stroke="#22a3c9" stroke-width="3" stroke-dasharray="2 2"/><text x="22" y="20" text-anchor="middle" font-size="8" font-weight="700" fill="#fff" font-family="Source Sans 3,Arial,sans-serif">NEW</text></svg>
  <div class="listing-head"><h3>2014 NORVAN KESTREL VERSA TDX</h3><p>Buy it now for € 13750 or please bid</p></div>
  <div class="thumb"><svg width="86" height="34" viewBox="0 0 86 34"><path d="M4 22l3-10 12-2 10-8h28l12 9 12 3 1 8H4z" fill="#a9a9a9"/><path d="M32 4h10v8H27zM45 4h10l8 8H45z" fill="#fff"/><circle cx="20" cy="26" r="7" fill="#a9a9a9" stroke="#fff" stroke-width="2"/><circle cx="66" cy="26" r="7" fill="#a9a9a9" stroke="#fff" stroke-width="2"/></svg></div>
  <div class="spec-row"><span>2007 (56)</span><span>58,000 Miles</span><span>Automatic</span><span>Grey</span></div>
  <ul class="col col-history"><h4><svg viewBox="0 0 10 10"><circle cx="5" cy="5" r="4" fill="none" stroke="#555" stroke-width="1.2"/><path d="M5 2.5V5h2" stroke="#555" fill="none"/></svg>HISTORY</h4><li>6 owners</li><li>NO SERVICE HISTORY</li><li>UK Vehicle</li><li class="strong">V5 NOT available due to cherished transfer</li></ul>
  <ul class="col col-seller"><h4><svg viewBox="0 0 10 10"><circle cx="5" cy="3" r="2.5" fill="#555"/><path d="M0 10a5 4 0 0 1 10 0z" fill="#555"/></svg>SELLER</h4><li>Specialist Dealer</li><li>East Yorkshire</li><li>214 Miles away</li><li>Joined 10 years ago</li><li>Holloway Vehicle Solutions Limited</li></ul>
  <p class="comments"><b>Comments:</b> Lorem Ipsum is simply dummy text of the printing and typesetting industry. Lorem Ipsum has been the industry's standard dummy text.</p>
  <div class="deal-box"><h5>Trying to Deal</h5><h6>My Customer</h6><div class="prices"><div class="price"><b>Trade Price</b>€ 15,750</div><div class="price"><b>Retail Price</b>€ 17,750</div></div><p class="guide">Guide Prices correct as of 02 Feb 2015</p><div class="details-btn">Full Details</div></div>
</article>

<div class="abs pager" style="top:1049px">
  <span class="wide">Prev</span><span class="current">1</span><span>2</span><span>3</span><span>4</span><span>5</span><span>6</span><span>7</span><span>8</span><span class="dots">...</span><span>25</span><span class="wide">Next</span>
</div>

<footer class="abs site-footer">
  <div class="foot-col" style="left:130px"><h4>ABOUT US</h4>Home<br>About Us<br>News<br>Privacy Policy</div>
  <div class="foot-col" style="left:248px;width:100px"><h4>TELL A FRIEND</h4>Tell your friends or collegues about Wheel Market Lane-email so they can also benefit from our services.</div>
  <div class="foot-col" style="left:394px"><h4>MORE INFORMATION</h4>Disclaimer<br>Sitemap<br>Privacy Policy</div>
  <div class="foot-col" style="left:520px"><h4>CONTACT</h4><b>Tel:</b> 120555 014732<br><b>Email:</b> customer@wheelmarketlane.com</div>
  <div class="foot-col" style="left:691px"><h4>FOLLOW US</h4><div class="socials"><i style="background:#3b5a9a"></i><i style="background:#2fa3dc"></i><i style="background:#d63a2f"></i></div></div>
</footer>
<div class="abs copyright">Copyright © 2015 wheelmarketlane.com. All Rights Reserved.</div>

</body>
</html>
```